Teams Background for client video calls - giving them a feel who we are

I'm keen to create a background artwork of a modern dynamic office that also reflects our values which are all about transparency, humility, integrity etc. Our company is called Quenby Collective. Our behaviours are agility, excellence and precision. You can find all about our colours and branding under our website www.quenbycollective.com

Target Market(s)

IT Recruitment

Industry/Entity Type

IT Recruitment

Font styles to use
Other font styles liked:
• as per our website www.quenbycollective.com

Colors
0054AA
0677BA
7BADD7
CADEEF
E8F1F8

Requirements
Must have
• A modern cool dynamic work office design incooperating our logo and what we stand for in terms of colours and our values and behaviours we live as a company. As i founded the office in the cabin but now we are in a modern office a blend would work i think.

```html
<!DOCTYPE html>
<html lang="en">
<head>
<meta charset="UTF-8">
<title>Quenby Collective – Video Call Background</title>
<link href="https://fonts.googleapis.com/css2?family=Josefin+Sans:wght@700&family=Oswald:wght@700&display=swap" rel="stylesheet">
<style>
  :root {
    --navy-deep: #020a4f;
    --navy-mid: #061660;
    --navy-light: #0c2a80;
    --blob-edge: #041258;
    --label-purple: #25196c;
    --label-teal: #00a29b;
    --text-white: #ffffff;
  }
  html, body {
    margin: 0;
    padding: 0;
    width: 1200px;
    height: 675px;
    overflow: hidden;
    background: var(--navy-deep);
  }
  .canvas {
    position: relative;
    width: 1200px;
    height: 675px;
    overflow: hidden;
    background: linear-gradient(100deg, var(--navy-deep) 0%, var(--navy-mid) 45%, var(--navy-light) 100%);
  }
  .backdrop-shape {
    position: absolute;
    inset: 0;
    width: 1200px;
    height: 675px;
  }
  .brand-name {
    position: absolute;
    left: 88px;
    top: 96px;
    margin: 0;
    font-family: "Josefin Sans", sans-serif;
    font-weight: 700;
    font-size: 30px;
    line-height: 1;
    color: var(--text-white);
    letter-spacing: 0.5px;
  }
  .behaviour {
    position: absolute;
    display: flex;
    align-items: center;
    justify-content: center;
    font-family: "Oswald", sans-serif;
    font-weight: 700;
    text-transform: uppercase;
    line-height: 1;
    box-shadow: 0 6px 14px rgba(0, 0, 20, 0.35);
  }
  .behaviour--precision {
    left: 456px;
    top: 402px;
    width: 310px;
    height: 108px;
    background: var(--label-purple);
    color: var(--label-teal);
    font-size: 66px;
    transform: rotate(1deg);
    align-items: flex-end;
    padding-bottom: 18px;
    box-sizing: border-box;
    letter-spacing: 0.5px;
  }
  .behaviour--agile {
    left: 458px;
    top: 168px;
    width: 276px;
    height: 122px;
    background: var(--label-purple);
    color: var(--label-teal);
    font-size: 104px;
    transform: rotate(-9deg);
    letter-spacing: 1px;
  }
  .behaviour--excellence {
    left: 397px;
    top: 283px;
    width: 416px;
    height: 121px;
    background: var(--label-teal);
    color: var(--text-white);
    font-size: 86px;
    transform: rotate(-3deg);
  }
</style>
</head>
<body>
  <main class="canvas">
    <svg class="backdrop-shape" viewBox="0 0 1200 675" aria-hidden="true">
      <defs>
        <linearGradient id="blobFill" x1="0" y1="0" x2="1" y2="1">
          <stop offset="0" stop-color="#0a2274" stop-opacity="0.35"/>
          <stop offset="1" stop-color="#0d2c86" stop-opacity="0.55"/>
        </linearGradient>
      </defs>
      <path d="M560 180 C 640 80, 820 20, 960 30 C 1100 40, 1160 140, 1140 260 C 1120 390, 1010 560, 830 650 C 700 700, 520 660, 460 560 C 410 470, 470 300, 560 180 Z"
            fill="url(#blobFill)" stroke="var(--blob-edge)" stroke-width="2.5"/>
      <path d="M1150 250 C 1170 380, 1080 560, 900 660" fill="none" stroke="#0e2f8c" stroke-opacity="0.5" stroke-width="8"/>
    </svg>

    <p class="brand-name">Quenby Collective</p>

    <div class="behaviour behaviour--precision">Precision</div>
    <div class="behaviour behaviour--agile">Agile</div>
    <div class="behaviour behaviour--excellence">Excellence</div>
  </main>
</body>
</html>
```